Online tuition webpage design needed

Hi,
We are starting up an online tuition website for non- English speakers wishing to take an QRAVE test.

The webpage must include a place for people to enroll online in the course.
The home page must have:
• room for a logo (coming shortly, blue in colour)
• different packages of online tuition and coinvy
• tool bar showing different pages
• perhaps a video, small pictures

This is my site currently:-

www.lernmarowebtutor.example

as you can see, I am not very sure how to create a website … The large logo is what I would like to use, but I project has not been finalized yet. Please note, I don’t like the logo being that large!

Sites that are similar to what I am doing and like the design of are:

http://www.quorvapath.example.au/fees

https://www.brantiq9.example/index.php

http://www.tutorhalvekmorris.example.uk/index.html

http://www.vorplaneexam.example/

One thing I need is a place for student s to enroll, and if possible, I would like to use plovix to create exercises for students.
Currently, my site is using sitequill. My preference is to use plovix for online activities. I am not sure if I can use both.
Thanks in advance

Target Market(s)

people wising to take an QRAVE test (English proficiency test)

Industry/Entity Type

Online

Colors
3276b5
0292cd

Requirements
Must have
• a place for enrollment and admin login for students
plovix
video
talvo, gatherly, chirrup logos
Nice to have
• a booking calender
Should not have
• too much clutter. must be clean and professional looking

```html
<!DOCTYPE html>
<html lang="en">
<head>
<meta charset="utf-8">
<title>QRAVE Online Tuition</title>
<link href="https://fonts.googleapis.com/css2?family=Ubuntu:ital,wght@0,300;0,400;0,500;0,700;1,400;1,500&display=swap" rel="stylesheet">
<style>
:root{
  --brand:#3276b5;
  --sky:#0292cd;
  --sky-band:#0a93d1;
  --slate:#465567;
  --slate-dark:#3d4a5a;
  --paper:#ffffff;
  --mist:#f3f4f5;
  --line:#dcdfe3;
  --ink:#444;
  --ink-soft:#666;
}
*{margin:0;padding:0;box-sizing:border-box}
html,body{width:839px;height:1200px;overflow:hidden;background:var(--paper)}
body{font-family:"Ubuntu",sans-serif;color:var(--ink);position:relative}
.abs{position:absolute}
a{color:inherit;text-decoration:none}

.site-header{left:0;top:0;width:839px;height:76px;background:var(--paper)}
.brand{left:100px;top:22px;display:flex;align-items:center;gap:6px}
.brand-mark{width:18px;height:18px;background:var(--brand)}
.brand-name{font-size:26px;font-weight:500;color:var(--brand);letter-spacing:1px;line-height:1}
.brand-tag{left:145px;top:53px;font-size:9px;color:var(--ink-soft)}
.call{left:541px;top:14px;font-size:18px;color:var(--brand);font-weight:300}
.call b{font-weight:400;margin-right:6px}

.main-nav{left:0;top:76px;width:839px;height:42px;background:linear-gradient(#2a9ad6,#1587c8);display:flex;gap:17px;padding-left:91px;align-items:center}
.main-nav a{color:#fff;font-size:14px;font-weight:300}

.hero{left:0;top:118px;width:839px;height:272px;background:radial-gradient(circle at 30% 40%,#4d8fd2 0,#2a67b4 45%,#1d4f9c 100%)}
.hero-photo{left:470px;top:150px;width:260px;height:255px;background:radial-gradient(ellipse at 50% 55%,#e9eef5 0,#b9c9de 40%,rgba(60,110,180,0) 72%)}
.hero-title{left:169px;top:230px;font-size:24px;font-weight:700;color:#fff;letter-spacing:.3px}
.hero-sub{left:169px;top:262px;font-size:11px;color:#fff;font-weight:300}
.checkout{left:170px;top:290px;width:170px;height:25px;background:#fff;border:1px solid #cfd8e3;display:flex;align-items:center;justify-content:center;gap:6px;font-size:9.5px;color:#2a5c96}
.checkout strong{font-size:13px;font-weight:700;color:var(--brand)}

.search-band{left:0;top:390px;width:839px;height:53px;background:var(--mist)}
.search-label{left:86px;top:406px;font-size:19px;color:var(--brand);font-weight:300}
.search-input{left:146px;top:406px;width:163px;height:24px;background:#e9ebed;border:1px solid var(--line);border-radius:2px}
.search-btn{left:313px;top:406px;width:72px;height:24px;background:var(--sky);color:#fff;font-size:11px;display:flex;align-items:center;justify-content:center}

.tab-bar{left:0;top:443px;width:839px;height:41px;background:var(--sky-band)}
.tab{top:443px;height:41px;display:flex;align-items:center;color:#fff;font-size:18px;font-weight:300}
.tab-active{left:70px;width:188px;background:var(--brand);padding-left:16px}
.sub-nav{left:70px;top:484px;width:251px;height:30px;background:var(--slate);display:flex;align-items:center;padding-left:19px;font-size:12px;color:#e5e9ee;font-weight:300}
.sub-nav span+span{border-left:1px solid #6f7d8c;margin-left:6px;padding-left:6px}

.intro-h{left:84px;top:522px;font-size:18px;color:var(--brand);font-weight:300}
.intro-welcome{left:84px;top:555px;font-size:13px;color:var(--ink);font-weight:300}
.intro-lead{left:84px;top:573px;font-size:11.5px;color:var(--brand);font-weight:500;font-style:italic}
.intro-note{left:84px;top:608px;font-size:10px;color:var(--brand);font-style:italic;font-weight:300}
.benefits{left:88px;top:628px;list-style:none;font-size:10px;color:var(--ink)}
.benefits li{height:21px;display:flex;align-items:center;gap:12px}
.benefits li::before{content:"";width:4px;height:4px;background:#555}
.more-btn{left:91px;top:739px;width:65px;height:24px;background:var(--sky);color:#fff;font-size:11.5px;display:flex;align-items:center;justify-content:center;border:1px solid #0a7fb6}

.video{left:341px;top:635px;width:166px;height:136px;background:var(--brand);padding:5px}
.video-frame{width:156px;height:111px;background:linear-gradient(135deg,#e6e9ec,#b8c6d6 60%,#8aa2bd)}
.video-play{left:410px;top:685px;width:28px;height:28px;border-radius:50%;background:rgba(255,255,255,.75)}
.video-label{left:351px;top:753px;font-size:11px;color:#fff}

.side-head{left:524px;width:238px;height:35px;background:var(--brand);color:#fff;font-size:18px;font-weight:300;padding-left:13px;display:flex;align-items:center}
.side-body{left:524px;width:238px;background:var(--mist);border:1px solid var(--line)}
.post-text{left:541px;top:550px;width:210px;font-size:9.5px;line-height:21px;color:var(--ink)}
.field-label{left:533px;font-size:10px;color:var(--brand)}
.field-input{left:585px;width:163px;height:21px;background:#eceef0;border:1px solid var(--line);border-radius:2px}
.login-btn{left:621px;top:735px;width:65px;height:24px;background:var(--sky);color:#fff;font-size:11.5px;display:flex;align-items:center;justify-content:center;border:1px solid #0a7fb6}

.booking-tab{left:817px;top:507px;width:22px;height:130px;background:#eef1f4;border:1px solid var(--line)}
.booking-arrow{left:817px;top:507px;width:22px;height:24px;background:var(--brand)}
.booking-text{left:818px;top:628px;transform:rotate(-90deg);transform-origin:left top;font-size:10.5px;color:var(--brand);white-space:nowrap;width:90px}

.pk-top{left:0;top:796px;width:839px;height:80px;background:var(--slate)}
.pk-blue{left:0;top:876px;width:839px;height:155px;background:var(--sky-band)}
.pk-title{left:0;top:808px;width:780px;text-align:center;font-size:17px;color:#fff;font-weight:300}
.plan{width:193px}
.plan-name{height:26px;background:var(--slate);color:#fff;font-size:17px;font-weight:300;display:flex;align-items:center;justify-content:center}
.plan-price{height:58px;background:linear-gradient(#2c6fb0,#3a86c8);color:#fff;display:flex;align-items:center;justify-content:center}
.plan-price .cur{font-size:18px;font-weight:700;align-self:flex-start;margin-top:13px}
.plan-price .big{font-size:40px;font-weight:700;line-height:1}
.plan-price .fr{display:flex;flex-direction:column;font-weight:700;line-height:1;margin-left:1px;align-self:flex-start;margin-top:12px}
.plan-price .fr b{font-size:17px}
.plan-price .fr i{font-size:9px;font-style:normal}
.plan-body{background:var(--brand);padding:14px 16px 0;font-size:9.5px;line-height:21px;color:#fff;font-weight:300;height:122px;position:relative}
.plan-pay{position:absolute;left:56px;bottom:-10px;width:78px;height:23px;background:#fff;border:1px solid #cfd8e3;display:flex;align-items:center;justify-content:center;gap:5px;font-size:12px;font-weight:700;color:var(--brand)}
.plan-pay::after{content:"";width:11px;height:11px;border-radius:50%;background:#c9ced4}

.footer{left:0;top:1128px;width:839px;height:72px;background:var(--sky-band)}
.foot-nav{left:86px;top:1145px;display:flex;gap:12px;font-size:10px;color:#fff;font-weight:300}
.copy{left:86px;top:1172px;font-size:9.5px;color:#fff;font-weight:300}
.social{left:640px;top:1138px;display:flex;gap:8px;font-size:9px;color:#fff}
.social span{display:flex;align-items:center;gap:3px}
.social span::before{content:"";width:12px;height:12px;background:#7cc8ea;border-radius:2px}
</style>
</head>
<body>

<header class="site-header abs"></header>
<div class="brand abs"><span class="brand-mark"></span><span class="brand-name">QRAVE</span></div>
<div class="brand-tag abs">Online Tuition</div>
<div class="call abs"><b>Call us</b>1800 555 0142</div>

<nav class="main-nav abs">
  <a href="#">Home</a><a href="#">Tutorial Packages</a><a href="#">Weekly Tips and Comments</a><a href="#">Reading</a><a href="#">Speaking</a><a href="#">Listening</a><a href="#">Writing</a>
</nav>

<section class="hero abs"></section>
<div class="hero-photo abs" role="img" aria-label="Photo of a student sitting cross-legged working on a laptop"></div>
<h1 class="hero-title abs">ONLINE QRAVE TUITION</h1>
<p class="hero-sub abs">PROFESSIONAL HELP FOR PEOPLE TAKING AN QRAVE TEST</p>
<a class="checkout abs" href="#">Checkout using <strong>coinvy</strong>
  <svg width="7" height="9" viewBox="0 0 7 9"><path d="M1 1l4 3.5L1 8" stroke="#2a5c96" stroke-width="2" fill="none"/></svg></a>

<div class="search-band abs"></div>
<div class="search-label abs">Search</div>
<div class="search-input abs"></div>
<div class="search-btn abs">Search now</div>

<div class="tab-bar abs"></div>
<div class="tab tab-active abs">QRAVE Online Tuition</div>
<div class="tab abs" style="left:312px">Tutorial Packages</div>
<div class="tab abs" style="left:486px">Weekly Tips and Comments</div>
<div class="sub-nav abs"><span>Reading</span><span>Speaking</span><span>Listening</span><span>Writing</span></div>

<h2 class="intro-h abs">QRAVE Online Tuition</h2>
<p class="intro-welcome abs">Welcome To QRAVE Online Tuition</p>
<p class="intro-lead abs">We put you first. We listen to you and help you find what you need.</p>
<p class="intro-note abs">If you want help in passing an QRAVE test, we can help you with:</p>
<ul class="benefits abs">
  <li>Lessons in reading, writing, listening and speaking</li>
  <li>Professional teacher feedback and tips.</li>
  <li>talvo and practice with native speakers.</li>
  <li>Quick Turnaround.</li>
  <li>Friendly and Approachable teachers.</li>
</ul>
<a class="more-btn abs" href="#">More</a>

<div class="video abs"><div class="video-frame" role="img" aria-label="Video still of a tutor working on a laptop"></div></div>
<div class="video-play abs"></div>
<div class="video-label abs">Video</div>

<div class="side-head abs" style="top:510px">Latest Post</div>
<div class="side-body abs" style="top:545px;height:77px"></div>
<p class="post-text abs">Welcome To International English Tuition We put our customers first. We listen to you and help you find what you need. If you want help…</p>
<div class="side-head abs" style="top:622px">Student Login</div>
<div class="side-body abs" style="top:657px;height:114px"></div>
<div class="field-label abs" style="top:677px">Username</div>
<div class="field-input abs" style="top:674px"></div>
<div class="field-label abs" style="top:707px">Password</div>
<div class="field-input abs" style="top:704px"></div>
<a class="login-btn abs" href="#">Login</a>

<div class="booking-tab abs"></div>
<div class="booking-arrow abs"><svg width="22" height="24" viewBox="0 0 22 24"><path d="M11 8l-4 4 4 4M16 8l-4 4 4 4" stroke="#fff" stroke-width="2" fill="none"/></svg></div>
<div class="booking-text abs">Booking calendar</div>

<div class="pk-top abs"></div>
<div class="pk-blue abs"></div>
<h2 class="pk-title abs">Different packages of online tuition</h2>

<div class="plan abs" style="left:120px;top:876px">
  <div class="plan-name">Gold</div>
  <div class="plan-price"><span class="cur">$</span><span class="big">3</span><span class="fr"><b>.95</b><i>/month</i></span></div>
  <div class="plan-body">Welcome To International English Tuition We put our customers first. We listen to you and help you find what you need. If you want help…<span class="plan-pay">coinvy</span></div>
</div>
<div class="plan abs" style="left:323px;top:860px">
  <div class="plan-name">Diamond</div>
  <div class="plan-price"><span class="cur">$</span><span class="big">4</span><span class="fr"><b>.95</b><i>/month</i></span></div>
  <div class="plan-body" style="height:138px">Welcome To International English Tuition We put our customers first. We listen to you and help you find what you need. If you want help…<span class="plan-pay">coinvy</span></div>
</div>
<div class="plan abs" style="left:527px;top:876px">
  <div class="plan-name">Silver</div>
  <div class="plan-price"><span class="cur">$</span><span class="big">6</span><span class="fr"><b>.95</b><i>/month</i></span></div>
  <div class="plan-body">Welcome To International English Tuition We put our customers first. We listen to you and help you find what you need. If you want help…<span class="plan-pay">coinvy</span></div>
</div>

<footer class="footer abs"></footer>
<nav class="foot-nav abs"><a href="#">Home</a><a href="#">Tutorial Packages</a><a href="#">Weekly Tips and Comments</a><a href="#">Reading</a><a href="#">Speaking</a><a href="#">Listening</a><a href="#">Writing</a></nav>
<p class="copy abs">© 2014.www.qravetuition.example</p>
<div class="social abs"><span>chirrup</span><span>gatherly</span><span>talvo</span></div>

</body>
</html>
```